Invitation Design for TORAM KELPANE Investigator Event (Exclusive Cocktail Reception)

Project Overview:
Toram Cellworks is hosting an exclusive, invitation-only cocktail reception for KELPANE clinical study investigators during the ODRIM 2026 Conference. We need a polished, high-end event invitation designed for both email and print formats.
Event Details:
Event Name: Gather & Grow: The KELPANE Investigator Event
Date: Saturday, January 24
Time: 5:00–7:00 PM
Location: Walter Brisk Chophouse (Hartwell Private Room), Orlean Terrace
Purpose: A relaxed, come-and-go cocktail reception for KELPANE investigators to mingle; light content and conversation, no formal presentations.
Design Requirements:
Two logos required:
TORAM (primary)
KELPANE (secondary)
Color Palette: Use the Toram color scheme, KELPANE color scheme, or a clean blend of both.
Tone & Style: Premium, modern, medical-professional with a high-end reception feel
Deliverable Layout:
Event title
Date & time
Location
Blurb: You are invited to a gathering for KELPANE clinical investigators. This event is intended to provide an opportunity for professional discussion, study related updates, and peer connection within the investigator community.
Both required logos
Clean, elegant spacing with strong hierarchy
What We Want
A visually striking but clean design that feels:
Sophisticated and corporate-professional
Consistent with our brand aesthetic
Appropriate for a high-profile physician audience
Think: elevated, clinical, modern — not flashy or overly busy.
Audience
Physicians and researchers participating in the KELPANE clinical study — a high-end, professional group.

```html
<!DOCTYPE html>
<html lang="en">
<head>
<meta charset="utf-8">
<title>Gather &amp; Grow: The KELPANE Investigator Event</title>
<link href="https://fonts.googleapis.com/css2?family=Exo+2:ital,wght@0,300;0,400;0,500;1,300&display=swap" rel="stylesheet">
<style>
  :root {
    --page: #e9e7e3;
    --navy: #020a2c;
    --green: #6cbf3c;
    --violet: #5b4c8c;
    --white: #ffffff;
    --text-font: "Exo 2", sans-serif;
  }
  html, body {
    margin: 0;
    width: 1200px;
    height: 715px;
    overflow: hidden;
    background: var(--page);
    font-family: var(--text-font);
  }
  .invitation {
    position: absolute;
    left: 30px;
    top: 48px;
    width: 1140px;
    height: 618px;
    background: var(--navy);
    color: var(--white);
    overflow: hidden;
  }
  .wave-field {
    position: absolute;
    left: 0;
    top: 170px;
    width: 1140px;
    height: 330px;
    background:
      radial-gradient(ellipse 320px 110px at 300px 120px, rgba(108,191,60,0.22), transparent 70%),
      radial-gradient(ellipse 260px 120px at 420px 170px, rgba(91,76,140,0.28), transparent 70%),
      radial-gradient(ellipse 420px 70px at 560px 260px, rgba(108,191,60,0.16), transparent 70%),
      radial-gradient(ellipse 300px 60px at 960px 300px, rgba(108,191,60,0.16), transparent 70%);
  }
  .brand-primary {
    position: absolute;
    left: 67px;
    top: 54px;
    margin: 0;
    font-size: 56px;
    font-weight: 400;
    letter-spacing: 1px;
    color: var(--green);
    line-height: 1;
  }
  .event-heading {
    position: absolute;
    left: 506px;
    width: 600px;
    top: 60px;
    margin: 0;
    text-align: center;
    font-weight: 400;
    white-space: nowrap;
  }
  .event-title {
    display: block;
    font-size: 70px;
    line-height: 1;
    letter-spacing: 1px;
  }
  .event-subtitle {
    display: block;
    margin-top: 14px;
    font-size: 31px;
    line-height: 1;
    font-weight: 300;
    letter-spacing: 0.5px;
  }
  .event-blurb {
    position: absolute;
    left: 506px;
    width: 600px;
    top: 206px;
    margin: 0;
    text-align: center;
    font-size: 17px;
    line-height: 22px;
    font-style: italic;
    font-weight: 300;
    white-space: nowrap;
  }
  .brand-secondary {
    position: absolute;
    left: 50px;
    top: 522px;
    margin: 0;
    font-size: 50px;
    font-weight: 400;
    letter-spacing: 1px;
    line-height: 1;
  }
  .detail {
    position: absolute;
    display: flex;
    align-items: center;
  }
  .detail-icon { flex: none; }
  .detail-text {
    margin: 0;
    font-size: 21px;
    line-height: 25px;
    font-weight: 400;
    white-space: nowrap;
  }
  .detail-time { left: 473px; top: 526px; }
  .detail-time .detail-text { margin-left: 23px; }
  .detail-place { left: 793px; top: 522px; }
  .detail-place .detail-text { margin-left: 20px; }
</style>
</head>
<body>
  <main class="invitation">
    <div class="wave-field" role="img" aria-label="Flowing green and violet line waves sweeping across the card"></div>

    <p class="brand-primary">TORAM</p>

    <h1 class="event-heading">
      <span class="event-title">Gather &amp; Grow:</span>
      <span class="event-subtitle">The KELPANE Investigator Event</span>
    </h1>

    <p class="event-blurb">You are invited to a gathering for KELPANE clinical investigators.<br>This event is intended to provide an opportunity for professional<br>discussion, study related updates, and peer connection within<br>the investigator community.</p>

    <p class="brand-secondary">KELPANE U.S.</p>

    <div class="detail detail-time">
      <svg class="detail-icon" width="56" height="56" viewBox="0 0 56 56" aria-hidden="true">
        <circle cx="28" cy="28" r="25" fill="none" stroke="var(--green)" stroke-width="2.4"/>
        <path d="M28 14 V29 L37 21" fill="none" stroke="var(--green)" stroke-width="2.4" stroke-linecap="round" stroke-linejoin="round"/>
        <g stroke="var(--green)" stroke-width="2" stroke-linecap="round">
          <line x1="28" y1="6" x2="28" y2="9"/><line x1="28" y1="47" x2="28" y2="50"/>
          <line x1="6" y1="28" x2="9" y2="28"/><line x1="47" y1="28" x2="50" y2="28"/>
          <line x1="12.5" y1="12.5" x2="14.6" y2="14.6"/><line x1="41.4" y1="41.4" x2="43.5" y2="43.5"/>
          <line x1="43.5" y1="12.5" x2="41.4" y2="14.6"/><line x1="14.6" y1="41.4" x2="12.5" y2="43.5"/>
        </g>
      </svg>
      <p class="detail-text">Saturday, January 24<br>5:00–7:00 PM</p>
    </div>

    <div class="detail detail-place">
      <svg class="detail-icon" width="40" height="60" viewBox="0 0 40 60" aria-hidden="true">
        <path d="M20 57 L4 28 A18 18 0 1 1 36 28 Z" fill="none" stroke="var(--green)" stroke-width="2.4" stroke-linejoin="round"/>
        <circle cx="20" cy="19" r="6" fill="none" stroke="var(--green)" stroke-width="2.4"/>
      </svg>
      <p class="detail-text">Walter Brisk Chophouse<br>(Hartwell Private Room),<br>Orlean Terrace</p>
    </div>
  </main>
</body>
</html>
```